Stationary for ultrasound imaging company
Business card, letter head, statonary envelope, fax cover sheet
Silver-Fern
Lino Varsek
Account Executive
20947 Marlow Pine Lane
Houston, TX 77095
linovarsek@postmeadow.com
at www.brisolavent.com
This is the logo for the company.

```html
<!DOCTYPE html>
<html lang="en">
<head>
<meta charset="utf-8">
<title>Silver-Fern Business Card</title>
<link href="https://fonts.googleapis.com/css2?family=Open+Sans:wght@400;600;700&display=swap" rel="stylesheet">
<style>
  :root {
    --bg: #e6e7e9;
    --card: #ffffff;
    --blue: #29a8e0;
    --navy: #1f3c78;
    --grey: #8a8d91;
    --grey-light: #d4d6d9;
    --ink: #2c2e31;
  }
  * { margin: 0; padding: 0; box-sizing: border-box; }
  html, body { width: 1200px; height: 871px; overflow: hidden; background: var(--bg); }
  body { font-family: "Open Sans", Arial, sans-serif; position: relative; }

  .card {
    position: absolute; left: 260px;
    width: 680px; height: 389px;
    background: var(--card);
    box-shadow: 0 5px 18px rgba(0,0,0,.12);
    overflow: hidden;
  }
  .card-back { top: 24px; }
  .card-front { top: 458px; }

  /* back face: logo only */
  .card-back .brand {
    position: absolute; left: 0; right: 0; top: 160px;
    display: flex; justify-content: center; align-items: center; gap: 16px;
  }
  .card-back .brand-square { width: 54px; height: 54px; }
  .card-back .brand-name { font-size: 56px; }

  .brand-square { background: var(--blue); flex: none; }
  .brand-name { font-weight: 700; color: var(--navy); letter-spacing: -1px; line-height: 1; }

  /* front face */
  .card-front .brand {
    position: absolute; left: 46px; top: 132px;
    display: flex; align-items: center; gap: 11px;
  }
  .card-front .brand-square { width: 38px; height: 38px; }
  .card-front .brand-name { font-size: 35px; }

  .divider {
    position: absolute; left: 300px; top: 75px;
    width: 1px; height: 177px; background: var(--grey-light);
  }

  .contact { position: absolute; left: 326px; top: 62px; color: var(--ink); }
  .person-name { font-size: 23px; font-weight: 600; color: var(--blue); line-height: 1.2; }
  .person-title { font-size: 15.5px; color: var(--grey); margin-bottom: 26px; }
  .address { font-size: 13.5px; line-height: 1.35; margin-bottom: 18px; }
  .lines { list-style: none; font-size: 13.5px; line-height: 1.55; }
  .lines li { display: flex; align-items: center; gap: 9px; }
  .lines svg { width: 11px; height: 11px; fill: var(--grey); flex: none; }

  .footer-wave { position: absolute; left: 0; bottom: 0; width: 680px; height: 122px; }
  .website {
    position: absolute; left: 0; right: 0; bottom: 20px;
    text-align: center; color: #fff; font-size: 13.5px; letter-spacing: 3.5px; font-weight: 600;
  }
</style>
</head>
<body>
  <div class="card card-back">
    <div class="brand">
      <div class="brand-square"></div>
      <div class="brand-name">Silver-Fern</div>
    </div>
  </div>

  <div class="card card-front">
    <div class="brand">
      <div class="brand-square"></div>
      <div class="brand-name">Silver-Fern</div>
    </div>

    <div class="divider"></div>

    <div class="contact">
      <div class="person-name">Lino Varsek</div>
      <div class="person-title">Account Executive</div>
      <div class="address">20947 Marlow Pine Lane<br>Houston, TX 77095</div>
      <ul class="lines">
        <li><svg viewBox="0 0 16 16"><path d="M3 1h3l1.5 4-2 1.5a9 9 0 0 0 4 4L11 8.5l4 1.5v3a2 2 0 0 1-2 2A12 12 0 0 1 1 3a2 2 0 0 1 2-2z"/></svg>713-555-0142</li>
        <li><svg viewBox="0 0 16 16"><rect x="4" y="1" width="8" height="14" rx="1.5"/></svg>314-555-0178</li>
        <li><svg viewBox="0 0 16 16"><rect x="1" y="5" width="14" height="9"/><rect x="4" y="1" width="8" height="5"/></svg>123-555-01934</li>
        <li><svg viewBox="0 0 16 16"><path d="M1 3h14v10H1z M1 3l7 6 7-6" stroke="#fff" stroke-width="1"/></svg>linovarsek@postmeadow.com</li>
      </ul>
    </div>

    <svg class="footer-wave" viewBox="0 0 1000 180" preserveAspectRatio="none" aria-hidden="true">
      <path d="M0 40 C300 110 700 110 1000 20 L1000 180 L0 180 Z" fill="var(--grey-light)"/>
      <path d="M0 75 C300 140 700 140 1000 55 L1000 180 L0 180 Z" fill="var(--blue)"/>
    </svg>
    <div class="website">www.brisolavent.com</div>
  </div>
</body>
</html>
```